Event Poster for Bar Sunday Live Music and Happy Hour

We are a bar. Every Sunday we have a HARBOUR HOURS event where we have live music and a Sunday Happy Hour. I would like a poster that promotes this weekly event in A4 and A3. Information the poster should include:Event Name: SUNDAY SESSIONSVenue: Copper Lantern 218-222 Marlow Rd PrestonDrink Specials: 3:00 pm - 5:00pmLive Music: 4:30pm -6:30pmAttached is our logo.

Target Market(s)

Both sexes 30-40 year olds

Industry/Entity Type

Hospitality

Font styles to use
Sans Serif

Colors

Designer to choose colors to be used in the design.

Requirements
Must have
• Event Name: HARBOUR HOURS
• Venue: Copper Lantern 218-222 Marlow Rd Preston
• Drink Specials: 3:00 pm - 5:00pm
• Live Music: 4:30pm -6:30pm
• Logo
Nice to have
• Open to different styles and ideas. Like colour.
Should not have
• It should not be too blokey are over the top bar-like.

```html
<!DOCTYPE html>
<html lang="en">
<head>
<meta charset="utf-8">
<title>Harbour Hours – Copper Lantern</title>
<link href="https://fonts.googleapis.com/css2?family=Oswald:wght@300;400;500;600&family=Yellowtail&display=swap" rel="stylesheet">
<style>
  :root{
    --page:#e9e7e3;
    --poster:#dcdbd9;
    --wall-light:#e4e3e1;
    --ink:#24272b;
    --maroon:#8a3a46;
    --rust:#a4553f;
    --script:#ebeae8;
    --badge:#2b3035;
    --white:#ffffff;
  }
  *{margin:0;padding:0;box-sizing:border-box}
  html,body{width:1200px;height:1200px;overflow:hidden;background:var(--page)}
  .poster{
    position:absolute;left:205px;top:41px;width:790px;height:1118px;
    background:linear-gradient(170deg,var(--wall-light),var(--poster) 60%,#d3d2d0);
    box-shadow:0 6px 24px rgba(0,0,0,.18);
    overflow:hidden;font-family:"Oswald",sans-serif;color:var(--ink);
  }
  .centered{position:absolute;left:0;right:0;text-align:center}
  .site-url{top:70px;font-size:13px;font-weight:400;letter-spacing:5px;color:#5a5c60}
  .brand-badge{
    position:absolute;top:100px;left:305px;width:180px;height:180px;border-radius:50%;
    background:var(--badge);display:flex;align-items:center;justify-content:center;
  }
  .brand-badge span{color:var(--white);font-size:24px;font-weight:400;letter-spacing:3px;line-height:1.25;text-align:center}
  .event-kicker{top:300px;font-size:66px;font-weight:400;letter-spacing:14px;color:var(--rust);z-index:2}
  .event-title{
    top:318px;font-family:"Yellowtail",cursive;font-size:250px;line-height:1;color:var(--script);
    text-shadow:2px 4px 6px rgba(0,0,0,.28);z-index:1
  }
  .frequency-band{
    position:absolute;top:545px;left:100px;width:590px;height:64px;border-radius:4px;
    background:var(--maroon);color:var(--white);display:flex;align-items:center;justify-content:center;
    font-size:30px;font-weight:400;letter-spacing:9px;box-shadow:0 3px 6px rgba(0,0,0,.25)
  }
  .schedule-line{font-size:46px;font-weight:400;letter-spacing:-0.5px;transform:scaleX(.82)}
  .schedule-line .time{color:var(--maroon);font-weight:500}
  .drinks{top:668px}
  .music{top:735px}
  .gallery{position:absolute;top:845px;left:90px;display:flex;gap:20px}
  .gallery .shot{width:190px;height:190px;border-radius:50%;border:3px solid var(--maroon)}
  .shot.food{background:radial-gradient(circle at 45% 45%,#8a8a6a,#3d3a35 70%)}
  .shot.bar{background:linear-gradient(180deg,#6b6e6c,#2f2d2a 70%,#1e1c1a)}
  .shot.dining{background:linear-gradient(180deg,#b9a68a,#6d5440 65%,#3a2a20)}
  .venue-name{top:1035px;font-size:38px;font-weight:500;letter-spacing:5px;color:var(--maroon)}
  .venue-address{top:1088px;font-size:15px;font-weight:600;letter-spacing:.5px;color:var(--ink)}
</style>
</head>
<body>
  <main class="poster">
    <p class="centered site-url">WWW.COPPERLANTERN.COM.AU</p>

    <div class="brand-badge"><span>COPPER<br>LANTERN</span></div>

    <h1>
      <span class="centered event-kicker">HARBOUR</span>
      <span class="centered event-title">Hours</span>
    </h1>

    <div class="frequency-band">• EVERY SUNDAY •</div>

    <p class="centered schedule-line drinks">DRINK SPECIALS <span class="time">3PM - 5PM</span></p>
    <p class="centered schedule-line music">LIVE MUSIC&nbsp; <span class="time">4:30PM - 6:30PM</span></p>

    <div class="gallery">
      <div class="shot food" role="img" aria-label="Overhead photo of shared plates of food on a wooden table"></div>
      <div class="shot bar" role="img" aria-label="Photo of the bar interior with high ceiling and counter"></div>
      <div class="shot dining" role="img" aria-label="Photo of the dining area with booths and pendant lights"></div>
    </div>

    <p class="centered venue-name">COPPER LANTERN</p>
    <p class="centered venue-address">218-222 MARLOW ROAD PRESTON</p>
  </main>
</body>
</html>
```